VOIP Telephony Flyer

I am looking for different design styles using my default flyer template and getting designers input and design views. <br/>You MUST use my default style template and make modifications but I would like the color scheme to remain the same. <br/>You MUST use the world grayed out back ground.<br/>You can modify the RED/BLACK color orientations based on your design.<br/>You must incorporate the telephone image as part of the illustration and leave room for 10 bullet points just as Features, PRICING, and contact information.<br/>Corner logo can be changed from location.<br/>design must meet 300dpi resolution for printing quality

```html
<!DOCTYPE html>
<html lang="en">
<head>
<meta charset="utf-8">
<title>Northline Voice – VoIP Telephony Flyer</title>
<link rel="stylesheet" href="https://fonts.googleapis.com/css2?family=Lato:wght@300;400;700&display=swap">
<style>
  :root {
    --stage: #3a3a3a;
    --navy-top: #0d4a69;
    --navy-bottom: #05283a;
    --red: #e31b2e;
    --white: #ffffff;
    --slate: #7a7a7a;
    --ink: #1d1d1f;
    --photo-light: #8a8f92;
    --photo-mid: #4b4f52;
    --photo-dark: #1e2022;
  }
  html, body {
    margin: 0;
    width: 1200px;
    height: 1200px;
    overflow: hidden;
    background: var(--stage);
  }
  .flyer {
    position: absolute;
    left: 262px;
    top: 129px;
    width: 687px;
    height: 962px;
    box-shadow: 0 10px 30px rgba(0,0,0,0.45);
  }
  .flyer svg { display: block; width: 100%; height: 100%; }
  .brand-name { font-family: 'Lato', sans-serif; font-weight: 300; fill: var(--white); letter-spacing: 2px; }
  .tag-label { font-family: 'Lato', sans-serif; font-weight: 700; fill: var(--white); }
  .feature-text { font-family: 'Lato', sans-serif; font-weight: 400; font-size: 15px; fill: var(--white); }
  .contact-phone { font-family: 'Lato', sans-serif; font-weight: 700; font-size: 29px; fill: #f2f2f2; }
  .contact-line { font-family: 'Lato', sans-serif; font-weight: 400; font-size: 14px; fill: #f2f2f2; }
</style>
</head>
<body>
<div class="flyer">
  <svg viewBox="0 0 858 1203" xmlns="http://www.w3.org/2000/svg">
    <defs>
      <linearGradient id="navyGradient" x1="0" y1="0" x2="0" y2="1">
        <stop offset="0" stop-color="var(--navy-top)"/>
        <stop offset="0.6" stop-color="#0a3e59"/>
        <stop offset="1" stop-color="var(--navy-bottom)"/>
      </linearGradient>
      <linearGradient id="photoGradient" x1="0" y1="0" x2="0.6" y2="1">
        <stop offset="0" stop-color="var(--photo-light)"/>
        <stop offset="0.45" stop-color="var(--photo-mid)"/>
        <stop offset="0.75" stop-color="var(--photo-dark)"/>
        <stop offset="1" stop-color="#3a3633"/>
      </linearGradient>
      <radialGradient id="mapGlow" cx="0.5" cy="0.5" r="0.5">
        <stop offset="0" stop-color="#ffffff" stop-opacity="0.09"/>
        <stop offset="1" stop-color="#ffffff" stop-opacity="0"/>
      </radialGradient>
    </defs>

    <!-- navy panel -->
    <rect class="navy-panel" width="858" height="1203" fill="url(#navyGradient)"/>

    <!-- faint world map background -->
    <rect class="world-map" x="400" y="280" width="458" height="440" fill="url(#mapGlow)"
          role="img" aria-label="Faint greyed-out world map background"/>

    <!-- office desk phone photograph -->
    <polygon class="phone-photo" points="0,0 22,0 858,1139 858,1203 0,1203"
             fill="url(#photoGradient)" role="img"
             aria-label="Photograph of a touchscreen VoIP desk phone on an office desk"/>

    <!-- diagonal bands -->
    <polygon class="band-white-top" points="0,0 32,0 177,229 162,247 0,22" fill="var(--white)"/>
    <polygon class="band-red" points="22,0 60,0 858,1109 858,1139" fill="var(--red)"/>
    <polygon class="band-white-bottom" points="422,609 437,587 858,1170 858,1203 837,1203" fill="var(--white)"/>
    <polygon class="contact-triangle" points="457,1203 647,939 837,1203" fill="var(--slate)"/>

    <!-- brand -->
    <circle class="brand-mark" cx="645" cy="101" r="37" fill="var(--ink)"/>
    <text class="brand-name" x="629" y="247" text-anchor="middle" font-size="50">NORTHLINE</text>
    <text class="brand-name" x="629" y="296" text-anchor="middle" font-size="50">VOICE</text>

    <!-- features -->
    <polygon class="tag" points="704,351 858,351 858,382 684,382" fill="var(--red)"/>
    <text class="tag-label" x="768" y="374" text-anchor="middle" font-size="25">Features</text>

    <g class="feature-list" text-anchor="end">
      <text class="feature-text" x="789" y="403">Lorem ipsum dolor sit amet, consectetur</text>
      <text class="feature-text" x="789" y="417">adipiscing elit, sed do eiusmod tempor</text>
      <circle cx="807" cy="405" r="3.5" fill="var(--white)"/>

      <text class="feature-text" x="792" y="456">Lorem ipsum dolor sit amet, consectetur</text>
      <text class="feature-text" x="792" y="470">adipiscing elit, sed do eiusmod tempor</text>
      <circle cx="807" cy="458" r="3.5" fill="var(--white)"/>

      <text class="feature-text" x="790" y="517">Lorem ipsum dolor sit amet, consectetur</text>
      <text class="feature-text" x="790" y="531">adipiscing elit, sed do eiusmod tempor</text>
      <circle cx="807" cy="521" r="3.5" fill="var(--white)"/>

      <text class="feature-text" x="788" y="579">Lorem ipsum dolor sit amet, consectetur</text>
      <text class="feature-text" x="788" y="593">adipiscing elit, sed do eiusmod tempor</text>
      <circle cx="807" cy="581" r="3.5" fill="var(--white)"/>

      <text class="feature-text" x="790" y="632">Lorem ipsum dolor sit amet, consectetur</text>
      <text class="feature-text" x="790" y="646">adipiscing elit, sed do eiusmod tempor</text>
      <circle cx="807" cy="634" r="3.5" fill="var(--white)"/>

      <text class="feature-text" x="788" y="685">Lorem ipsum dolor sit amet,</text>
      <text class="feature-text" x="788" y="699">consectetur adipiscing elit, sed</text>
      <text class="feature-text" x="788" y="713">do eiusmod tempor</text>
      <circle cx="807" cy="682" r="3.5" fill="var(--white)"/>
    </g>

    <!-- prices -->
    <polygon class="tag" points="739,749 858,749 858,780 719,780" fill="var(--red)"/>
    <text class="tag-label" x="793" y="772" text-anchor="middle" font-size="25">Prices</text>

    <!-- contact -->
    <polygon class="tag" points="630,1057 757,1057 757,1087 612,1087" fill="var(--red)"/>
    <text class="tag-label" x="685" y="1079" text-anchor="middle" font-size="20">Contact Us</text>
    <text class="contact-phone" x="759" y="1120" text-anchor="end">555 - 014 - 2290</text>
    <text class="contact-line" x="759" y="1139" text-anchor="end">www.northlinevoice.example</text>
    <text class="contact-line" x="759" y="1156" text-anchor="end">2240 Harbor Lane Suite 310 Bayview Florida 33000</text>
  </svg>
</div>
</body>
</html>
```